IT Company Business Card Design w/Stationary Design

We have a great logo we like! We are looking to redesign our business cards and all company logo'd merchandise/materials.

We are an IT Company located near the Bay Area (San Francisco, CA). We specialize in Managed Services and offer complete IT Computer and Network Support to Businesses of all sizes. We thrive on making a lasting impression. We have been doing IT for 15yrs+ but are young at heart. We like to stand out and be different. We want to be unique and have a recognizable brand. We need our logo to represent who we are. We are young, professional, creative and outstanding. We don't want to blend in, we want to stand out. Our business card needs to stand out and grab attention. Something Bold, yet simple and clean. (I will provide ideas of what we like to give a taste of what we are looking for).

The design can include any kind of texture/artistic design or sizing EXCEPT please "no square card designs" as they don't seem to fit in wallets very well. We dont mind curved edges, rounded corners, vertical layouts or horizontal layouts, embossing, letter press or raised surfaces. Again, we dont want to look average or plain or boring. :) Be creative - yet practical! We have ordered from Pebblecraft designs before and been very happy. Their card sizes tend to be a little different, so beware. Hope this helps!

Target Market(s)

Businesses - Small to Medium, Corporations, Publicly Traded Companies

Industry/Entity Type

Business

Contact Information for Business Card

Harbor Lantern IT
7318 Quillby Avenue
Suite F
Modesto, CA 95871

Office 209.555.0137
Direct 209.555.0182
Cell 209.555.0164

Ross Tavener
Founder, CEO
www.hlit-example.com
rtavener@hlit-example.com

Locations Serviced: Modesto, Stockton, Pleasanton, Fresno (incorporate this on the card ONLY if there's a good place to do so).

What we specialize in: Computer, Network, Voice, Data. (IT Services)

Our Logo Colors: Black and Blue (#006699). Open to using grey or orange as well - but not required. Don't want too busy....

Logo Font: "Cinthe" (Will attach logo font). We want type style to be clean. You can show different font types including our logo font - and we are open to other font ideas.

The logo can be separated. You can use elements together or apart. Surprise us! :) We "REALLY" want the "hl" to be our identifier/our brand people recognize.

Font styles to use
Sans Serif

Colors
0355a3
3176b5
f37122
f78f20
faa54b
474747
aaaaaa
757575
000000

Requirements
Must have
• Bold, Big, Colorful, Modern/yet Fun, Clean Design, Stand Out Presence, Texture would be welcomed - but not necessary, Card design shape can include cut corners or rounded or square edges. Be creative. (HOWEVER, we don't want a square design because we have found it doesn't fit in wallets that easily).
• We do like using Pebblecraft printing company (Which they have particular sizing on their card templates - beware), but are open to other design templates/printing companies as well. We just want to make sure its easy to find a print company to do our work. Too unique could be costly and hard to get cards printed.
• Colors to use: Our logo Blue (#006699), with either whites, grays, black, shades of our blue, and maybe a pinch of orange if needed. Primarily, blue, white, gray or black.
Nice to have
• Texture would be cool or little different edging or shape - but nothing too costly to print. I have seen cards with 3 sharp edges and one round edge. Something like that would be cool as an option. Or a vertical card.
• I love a faded watermark look. It would be nice to see some shading of our circle logo on a few designs. The circle with "hl" in it OR.... taking just the "hl" and using it alone.
Should not have
• No square card designs. Nothing too expensive or elaborate to print. No busy fonts. Do not like Times New Roman type fonts (too old looking). Not a lot of orange (if you even choose to use some orange).

```html
<!DOCTYPE html>
<html lang="en">
<head>
<meta charset="utf-8">
<title>Harbor Lantern IT – Business Card</title>
<link href="https://fonts.googleapis.com/css2?family=Lato:wght@300;400;700&display=swap" rel="stylesheet">
<style>
  :root {
    --brand-blue: #1a8fc9;
    --brand-blue-deep: #0b6fa8;
    --brand-blue-light: #3aa7dc;
    --accent-orange: #f78f20;
    --accent-grey: #757575;
    --text-dark: #474747;
    --card-white: #ffffff;
    --page-bg: #ebe8e3;
  }
  html, body {
    margin: 0;
    width: 1200px;
    height: 1023px;
    overflow: hidden;
    background: var(--page-bg);
    font-family: "Lato", sans-serif;
  }
  .stage {
    position: relative;
    width: 1200px;
    height: 1023px;
  }
  .card {
    position: absolute;
    width: 560px;
    height: 320px;
    border-radius: 18px;
    overflow: hidden;
    box-shadow: 0 10px 30px rgba(0,0,0,0.18);
  }
  .card-front { left: 60px; top: 120px; background: var(--card-white); }
  .card-back  { left: 580px; top: 583px; }
  .card svg { display: block; }
  .wordmark { font-family: "Lato", sans-serif; font-weight: 700; fill: var(--brand-blue); font-size: 22px; }
  .person-name { font-weight: 700; font-size: 17px; fill: var(--brand-blue); }
  .person-title { font-weight: 400; font-size: 13px; fill: var(--accent-grey); }
  .contact { font-size: 11.5px; fill: var(--text-dark); font-weight: 400; }
  .locations-label { font-size: 12.5px; font-weight: 700; fill: var(--brand-blue); }
  .specialty { font-size: 11px; fill: #fff; font-weight: 400; }
  .back-wordmark { font-weight: 700; font-size: 40px; fill: #fff; letter-spacing: 1px; }
  .back-url { font-size: 13px; fill: #fff; font-weight: 400; }
</style>
</head>
<body>
<main class="stage">

  <!-- Front of card -->
  <section class="card card-front" aria-label="Business card front">
    <svg width="560" height="320" viewBox="0 0 560 320">
      <defs>
        <linearGradient id="band-blue" x1="0" y1="0" x2="1" y2="1">
          <stop offset="0" stop-color="var(--brand-blue-light)"/>
          <stop offset="1" stop-color="var(--brand-blue-deep)"/>
        </linearGradient>
      </defs>

      <!-- left brand band -->
      <path class="side-band" d="M0 0 H70 C60 120 110 230 200 320 H0 Z" fill="url(#band-blue)"/>
      <path class="side-sliver" d="M70 0 H90 C85 120 130 230 215 320 H200 C110 230 60 120 70 0 Z" fill="var(--accent-grey)"/>

      <!-- bottom swoosh -->
      <path class="swoosh-grey" d="M200 320 C350 296 480 240 560 160 V172 C485 250 360 304 220 320 Z" fill="var(--accent-grey)"/>
      <path class="swoosh-orange" d="M220 320 C360 304 485 250 560 172 V188 C490 255 375 308 240 320 Z" fill="var(--accent-orange)"/>
      <path class="swoosh-blue" d="M240 320 C375 308 490 255 560 188 V320 Z" fill="url(#band-blue)"/>

      <!-- brand mark -->
      <circle cx="80" cy="140" r="50" fill="var(--brand-blue)" stroke="#fff" stroke-width="4"/>
      <text class="wordmark" x="145" y="148">Harbor Lantern IT</text>

      <!-- name -->
      <text class="person-name" x="172" y="246">Ross Tavener</text>
      <text class="person-title" x="172" y="264">Founder, CEO</text>

      <!-- contact block -->
      <g text-anchor="end">
        <text class="contact" x="540" y="34">7318 Quillby Avenue Suite F</text>
        <text class="contact" x="540" y="50">Modesto, CA 95871</text>
        <text class="contact" x="522" y="74">209.555.0164</text>
        <text class="contact" x="522" y="90">209.555.0137 (Office)</text>
        <text class="contact" x="522" y="106">209.555.0182 (Direct)</text>
        <text class="contact" x="522" y="122">rtavener@hlit-example.com</text>
        <text class="locations-label" x="540" y="146">Locations Serviced:</text>
        <text class="contact" x="522" y="162">Modesto, Stockton, Pleasanton, Fresno.</text>
      </g>
      <g class="contact-icons" fill="var(--brand-blue)">
        <rect x="529" y="65" width="11" height="11" rx="2"/>
        <rect x="529" y="81" width="11" height="11" rx="2" fill="none" stroke="var(--brand-blue)" stroke-width="1.5"/>
        <rect x="529" y="97" width="11" height="11" rx="2" fill="none" stroke="var(--brand-blue)" stroke-width="1.5"/>
        <rect x="529" y="113" width="11" height="11" rx="2"/>
        <path d="M531 116 L534.5 119.5 L538 116" stroke="#fff" stroke-width="1.2" fill="none"/>
      </g>

      <!-- specialties -->
      <g text-anchor="end">
        <text class="specialty" x="540" y="286">We specialize in:</text>
        <text class="specialty" x="540" y="303">Computer, Network, Voice, Data.</text>
      </g>
    </svg>
  </section>

  <!-- Back of card -->
  <section class="card card-back" aria-label="Business card back">
    <svg width="560" height="320" viewBox="0 0 560 320">
      <defs>
        <linearGradient id="back-blue" x1="0" y1="0" x2="1" y2="1">
          <stop offset="0" stop-color="var(--brand-blue-light)"/>
          <stop offset="1" stop-color="var(--brand-blue-deep)"/>
        </linearGradient>
      </defs>
      <rect width="560" height="320" fill="url(#back-blue)" role="img" aria-label="Faint repeating brand-mark pattern across a blue field"/>
      <circle cx="150" cy="150" r="34" fill="#fff"/>
      <text class="back-wordmark" x="198" y="164">Harbor Lantern</text>
      <text class="back-url" x="30" y="296">www.hlit-example.com</text>
    </svg>
  </section>

</main>
</body>
</html>
```